Lantern - Web Design Project

We are seeking to have our website redesigned. Our current webpage is rather dated looking www.lantern-outcomes.com We will be utilizing similar content to explain our services as what is in the website now. We do not see it at a retail portal but rather a website for those inquiring about our services as a reference check so to speak.

We wish to have a look that is considered clean, fresh, contemporary and contains a business savvy vibe.

We prefer isolated white background and also wish to retain the integrity of our Logo and colour scheme.

We are looking for something that doesnt look like it was designed at home on sitemoose. We are hoping to find something that looks like it would reside on a tablet.
Updates

Hello designers!

We apologize for our tardiness as we have been quite preoccupied. We will be extending our invites to the end of January!

Hello All,

Please review our offer once again for updated requirements.  We are hoping to accept a design by months end.

Lantern

Target Market(s)

Business to business clients and Large manufacturers

Industry/Entity Type

Retail

Requirements
Must have
• Existing Logo

There must be an area dedicated to an intro video that will be incorporated on our landing page.

We require design of the other pages as well not only the landing page.

```html
<!DOCTYPE html>
<html lang="en">
<head>
<meta charset="utf-8">
<title>Lantern Performance Group</title>
<link href="https://fonts.googleapis.com/css2?family=Arimo:wght@400;700&family=Roboto+Condensed:ital,wght@0,300;0,400;1,700&display=swap" rel="stylesheet">
<style>
:root{
  --ink:#222;
  --grey:#555;
  --red:#d91a1a;
  --nav-top:#5a5a5a;
  --nav-bot:#1e1e1e;
  --band:#efedee;
  --panel:#f2f1f1;
  --footer:#222;
}
*{margin:0;padding:0;box-sizing:border-box}
html,body{width:1200px;height:1170px;overflow:hidden;background:#fff}
body{position:relative;font-family:"Arimo",Arial,sans-serif;color:var(--ink)}
.abs{position:absolute}
.logo{left:134px;top:22px;display:flex;align-items:center;gap:8px}
.logo-mark{width:18px;height:18px;border-radius:50%;background:var(--red)}
.logo-name{font-size:46px;color:#555;font-weight:400;letter-spacing:-1px}
.phone{right:132px;top:42px;font-size:22px;color:#444}
.phone b{font-family:"Roboto Condensed",sans-serif;font-style:italic;font-weight:700;font-size:19px}
.nav{left:132px;top:102px;width:936px;height:40px;border-radius:10px;background:linear-gradient(var(--nav-top),var(--nav-bot));display:flex;align-items:center;overflow:hidden}
.nav a{flex:none;color:#fff;text-decoration:none;font-size:13px;height:40px;line-height:40px;text-align:center;white-space:nowrap;border-right:1px solid #6a6a6a}
.nav a.home{background:#1a1a1a}
.search{flex:none;margin-left:2px;width:157px;height:26px;background:#fff;font-size:11px;color:#555;padding:9px 4px 0}
.search-btn{flex:none;width:36px;height:26px;background:linear-gradient(#f26a6a,#b81010)}
.slider{left:132px;top:143px;width:936px;height:318px;background:linear-gradient(#777,#444);border-radius:4px}
.slide{left:10px;top:7px;width:916px;height:304px;border-radius:6px;overflow:hidden;background:linear-gradient(170deg,#07152e 0%,#0d3d78 45%,#1b5aa0 70%,#0a1a33 100%)}
.arrow{top:134px;width:50px;height:40px;background:#d8d8d8;opacity:.9;display:flex;align-items:center;justify-content:center}
.caption{left:0;bottom:0;width:916px;height:89px;background:rgba(200,200,215,.72);padding:12px 12px;font-size:18.5px;line-height:24px;color:#111}
.caption i{font-family:"Roboto Condensed",sans-serif;font-weight:700;font-size:17px;color:#333}
.card{top:474px;width:272px;height:249px}
.card-frame{left:8px;top:0;width:256px;height:249px;border:1px solid #777;border-radius:8px;background:#fff}
.card-head{left:0;top:14px;width:272px;height:40px;background:linear-gradient(#555,#2a2a2a);color:#fff;font-family:"Roboto Condensed",sans-serif;font-style:italic;font-weight:700;font-size:17px;line-height:40px;text-align:center;white-space:nowrap}
.card-text{left:16px;top:58px;width:240px;font-family:"Roboto Condensed",sans-serif;font-weight:300;font-size:13px;line-height:17px;color:#333}
.card-photo{left:17px;top:138px;width:234px;height:104px;border:1px solid #888;background:linear-gradient(135deg,#c9d2dc,#8c98a8 50%,#e6e4e0)}
.band{left:0;top:738px;width:1200px;height:187px;background:var(--band);border-top:1px solid #ddd;border-bottom:1px solid #ddd}
.main{left:132px;top:760px;width:936px;height:307px;background:var(--panel);box-shadow:0 0 6px rgba(0,0,0,.25)}
.welcome{left:12px;top:10px;font-size:18px;color:#333;font-weight:400}
.welcome b{font-family:"Roboto Condensed",sans-serif;font-style:italic;font-weight:700;color:var(--red)}
.copy{left:12px;top:40px;width:664px;font-size:12.2px;line-height:15px;color:#222}
.copy p{margin-bottom:8px}
.contact{left:822px;top:773px;width:244px;height:262px}
.contact-frame{left:0;top:0;width:236px;height:262px;border:1px solid #777;border-radius:8px;background:#fff}
.contact-head{left:-7px;top:12px;width:250px;height:36px;background:linear-gradient(#555,#2a2a2a);color:#fff;font-family:"Roboto Condensed",sans-serif;font-style:italic;font-weight:700;font-size:20px;line-height:36px;text-align:center}
.label{left:10px;font-size:12px;color:#333}
.field{left:6px;width:214px;height:28px;border:1px solid #aaa;background:#fff}
.submit{left:146px;top:222px;width:78px;height:26px;background:linear-gradient(#555,#222);color:#fff;font-size:16px;text-align:center;line-height:26px}
.redline{left:0;top:1066px;width:1200px;height:6px;background:var(--red)}
.footer{left:0;top:1072px;width:1200px;height:98px;background:var(--footer)}
.social{top:18px;width:31px;height:31px;border-radius:4px;background:#4a86b8}
.legal{left:141px;top:78px;font-size:9.5px;color:#bbb;white-space:nowrap}
</style>
</head>
<body>
<header>
  <div class="abs logo"><span class="logo-name">lantern</span><span class="logo-mark"></span></div>
  <div class="abs phone"><b>CAll</b> :+1.800.555.0148</div>
  <nav class="abs nav">
    <a class="home" style="width:68px">Home</a><a style="width:112px">Who we are</a><a style="width:142px">Cross the lantern</a><a style="width:160px">Perfomence solution</a><a style="width:140px">Sustain solution</a><a style="width:82px;border:none">Join us</a>
    <div class="search">Search........</div><div class="search-btn"></div>
  </nav>
</header>

<section class="abs slider">
  <div class="abs slide" role="img" aria-label="Illuminated steel arch bridge over a harbour at night">
    <div class="abs arrow" style="left:0"><svg width="14" height="26"><path d="M12 2 L2 13 L12 24" stroke="#444" stroke-width="2.5" fill="none"/></svg></div>
    <div class="abs arrow" style="right:0"><svg width="14" height="26"><path d="M2 2 L12 13 L2 24" stroke="#444" stroke-width="2.5" fill="none"/></svg></div>
    <div class="abs caption">"There are managers so preoccupied with their e-mail messages that they never look up from their screens to see what's happening in the nondigital world."<br><i>- Marten Ostrova</i></div>
  </div>
</section>

<section>
  <div class="abs card" style="left:127px">
    <div class="abs card-frame"></div>
    <div class="abs card-head">Experienced performance consultants</div>
    <div class="abs card-text">Lorem ipsum dolor sit amet, consectetur adipisicing elit, sed do eiusmod tempor incididunt ut labore et doloreexercitation ullamco laboris nisi ut a consequa</div>
    <div class="abs card-photo" role="img" aria-label="Team of consultants working at a meeting table"></div>
  </div>
  <div class="abs card" style="left:466px">
    <div class="abs card-frame"></div>
    <div class="abs card-head">Experienced performance consultants</div>
    <div class="abs card-text">Lorem ipsum dolor sit amet, consectetur adipisicing elit, sed do eiusmod tempor incididunt ut labore et doloreexercitation ullamco laboris nisi ut a consequa</div>
    <div class="abs card-photo" role="img" aria-label="Team of consultants working at a meeting table"></div>
  </div>
  <div class="abs card" style="left:805px">
    <div class="abs card-frame"></div>
    <div class="abs card-head">Experienced performance consultants</div>
    <div class="abs card-text">Lorem ipsum dolor sit amet, consectetur adipisicing elit, sed do eiusmod tempor incididunt ut labore et doloreexercitation ullamco laboris nisi ut a consequa</div>
    <div class="abs card-photo" role="img" aria-label="Team of consultants working at a meeting table"></div>
  </div>
</section>

<div class="abs band"></div>
<main class="abs main">
  <h1 class="abs welcome">Welcome to <b>Lantern Performance Group</b></h1>
  <div class="abs copy">
    <p>Lorem ipsum dolor sit amet, consectetur adipisicing elit, sed do eiusmod tempor incididunt ut labore et dolore magna aliqua. Ut enim ad minim veniam, quis nostrud exercitation ullamco laboris nisi ut aliquip ex ea commodo consequat. Duis aute irure dolor in reprehenderit in voluptate velit esse cillum dolore eu fugiat nulla pariatur. Excepteur sint occaecat cupidatat non proident, sunt in culpa qui officia deserunt mollit anim id est laborum</p>
    <p>Lorem ipsum dolor sit amet, consectetur adipisicing elit, sed do eiusmod tempor incididunt ut labore et dolore magna aliqua. Ut enim ad minim veniam, quis nostrud exercitation ullamco laboris nisi ut aliquip ex ea commodo consequat. Duis aute irure dolor in reprehenderit in voluptate velit esse cillum dolore eu fugiat nulla pariatur. Excepteur sint occaecat cupidatat non proident, sunt in culpa qui officia deserunt mollit anim id est laborum</p>
    <p>Lorem ipsum dolor sit amet, consectetur adipisicing elit, sed do eiusmod tempor incididunt ut labore et dolore magna aliqua. Ut enim ad minim veniam, quis nostrud exercitation ullamco laboris nisi ut aliquip ex ea commodo consequat. Duis aute irure dolor in reprehenderit in voluptate velit esse cillum dolore eu fugiat nulla pariatur. Excepteur sint occaecat cupidatat non proident, sunt in culpa qui officia deserunt mollit anim id est laborum</p>
  </div>
</main>

<aside class="abs contact">
  <div class="abs contact-frame"></div>
  <div class="abs contact-head">Contact Us</div>
  <div class="abs label" style="top:58px">NAME</div>
  <div class="abs field" style="top:70px"></div>
  <div class="abs label" style="top:102px">EMAIL</div>
  <div class="abs field" style="top:114px"></div>
  <div class="abs label" style="top:146px">MESSAGE</div>
  <div class="abs field" style="top:158px;width:222px;height:60px"></div>
  <div class="abs submit">Submit</div>
</aside>

<div class="abs redline"></div>
<footer class="abs footer">
  <div class="abs social" style="left:133px" role="img" aria-label="Professional network profile"></div>
  <div class="abs social" style="left:175px" role="img" aria-label="Microblog profile"></div>
  <div class="abs social" style="left:217px" role="img" aria-label="Social network profile"></div>
  <div class="abs legal">Copyright 2011. All rights reserved. &nbsp;| &nbsp;Lantern Performance Group &nbsp;| &nbsp;48 Harrow Lane, Kingsford, ON K2P 0Z9, Canada &nbsp;T :+1.800.555.0148 &nbsp;Email:info@lantern-outcomes.com | &nbsp;Site Map</div>
</footer>
</body>
</html>
```